Corrindale Planners, LLC Stationary

Corrindale Planners, LLC is a new financial planning and consulting company. We are looking for designs on business cards, letterhead, envelopes, and anything else that would be useful. Our preference for business card design is two sided. We are looking for a professional and clean look with incorporating the logo and patriotic feel. Thank you to all who participate and good luck!

```html
<!DOCTYPE html>
<html lang="en">
<head>
<meta charset="utf-8">
<title>Corrindale Planners, LLC Stationery</title>
<link rel="stylesheet" href="https://fonts.googleapis.com/css2?family=Arimo:wght@400;600;700&display=swap">
<style>
  :root{
    --navy:#123f6b;
    --red:#c3222b;
    --paper:#f4f3f1;
    --white:#ffffff;
    --ink:#4a4a4a;
    --backdrop:#a9a7a7;
    --shadow:2px 3px 6px rgba(0,0,0,.35);
  }
  *{margin:0;padding:0;box-sizing:border-box}
  html,body{width:1200px;height:770px;overflow:hidden;background:var(--backdrop);font-family:"Arimo",Arial,sans-serif}
  .sheet{position:absolute;overflow:hidden;box-shadow:var(--shadow);background:var(--paper)}
  .sheet svg.curves{position:absolute;left:0;top:0}
  .brand{position:absolute;display:flex;align-items:center;gap:6px;color:var(--navy);font-weight:700;white-space:nowrap;letter-spacing:.02em}
  .brand .dot{border-radius:50%;background:var(--navy);flex:none}
  .brand.light{color:var(--white)}
  .brand.light .dot{background:var(--white)}
  .address{position:absolute;color:var(--ink);line-height:1.35}
  .contacts{position:absolute;list-style:none;color:var(--ink);line-height:1.4}
  .contacts li{display:flex;align-items:center;gap:4px}
  .contacts svg{fill:var(--navy);flex:none}
  .web{position:absolute;color:var(--white);letter-spacing:.12em;text-align:center;width:100%}
  .faint-mark{position:absolute;border-radius:50%;background:rgba(18,63,107,.06)}

  /* business card front */
  .card-front{left:86px;top:46px;width:218px;height:124px;background:var(--white)}
  .card-front .brand{left:14px;top:22px;font-size:11px}
  .card-front .brand .dot{width:9px;height:9px}
  .card-front .address{left:14px;top:62px;font-size:5.6px}
  .card-front .contacts{left:14px;top:82px;font-size:5.6px}
  .card-front .person{position:absolute;right:36px;top:65px;text-align:right}
  .person .name{color:var(--navy);font-size:7.5px;font-weight:600}
  .person .role{color:var(--red);font-size:5.6px}

  /* business card back */
  .card-back{left:338px;top:46px;width:218px;height:124px;background:var(--navy)}
  .card-back .brand{left:0;right:0;justify-content:center;top:50px;font-size:11px}
  .card-back .brand .dot{width:9px;height:9px}
  .card-back .web{top:106px;font-size:5.5px}

  /* envelope front */
  .envelope-front{left:61px;top:202px;width:562px;height:255px}
  .envelope-front .brand{left:25px;top:30px;font-size:15px}
  .envelope-front .brand .dot{width:12px;height:12px}
  .envelope-front .address{left:25px;top:67px;font-size:9px}
  .envelope-front .faint-mark{left:330px;top:20px;width:210px;height:210px}

  /* envelope back */
  .envelope-back{left:56px;top:479px;width:560px;height:255px}
  .envelope-back .brand{left:0;right:0;justify-content:center;top:34px;font-size:12px}
  .envelope-back .brand .dot{width:10px;height:10px}
  .envelope-back .web{top:70px;font-size:7px}

  /* letterhead */
  .letterhead{left:643px;top:33px;width:497px;height:701px}
  .letterhead .brand{left:32px;top:52px;font-size:15px}
  .letterhead .brand .dot{width:12px;height:12px}
  .letterhead .address{left:370px;top:23px;font-size:8.5px}
  .letterhead .contacts{left:370px;top:48px;font-size:8.5px;line-height:1.45}
  .letterhead .faint-mark{left:90px;top:200px;width:330px;height:330px}
</style>
</head>
<body>

<section class="sheet card-front" aria-label="Business card, front">
  <svg class="curves" width="218" height="124" viewBox="0 0 218 124" aria-hidden="true">
    <rect width="218" height="124" fill="var(--navy)"/>
    <path d="M0 0H200C236 26 236 100 186 124H0Z" fill="var(--red)"/>
    <path d="M0 0H164C214 22 226 100 176 124H0Z" fill="var(--white)"/>
  </svg>
  <div class="brand"><span class="dot"></span>Corrindale Planners, LLC</div>
  <p class="address">2170 Linden Court<br>Ashgrove, NY 11620</p>
  <ul class="contacts">
    <li><svg width="5" height="5" viewBox="0 0 10 10"><path d="M1 3Q5 0 9 3L8 5 6 4V3H4V4L2 5Z M2 6H8V9H2Z"/></svg>555 0142 7788</li>
    <li><svg width="5" height="5" viewBox="0 0 10 10"><path d="M3 1H7V3H3Z M1 4H9V8H1Z"/></svg>555 0198 3310</li>
    <li><svg width="5" height="5" viewBox="0 0 10 10"><path d="M0 2H10V8H0Z" /></svg>marcus@corrindale.com</li>
    <li><svg width="5" height="5" viewBox="0 0 10 10"><circle cx="5" cy="5" r="5"/></svg>www.corrindaleplanners.com</li>
  </ul>
  <div class="person"><p class="name">MARCUS HALE</p><p class="role">PRESIDENT</p></div>
</section>

<section class="sheet card-back" aria-label="Business card, back">
  <div class="brand light"><span class="dot"></span>Corrindale Planners, LLC</div>
  <p class="web">www.corrindaleplanners.com</p>
</section>

<section class="sheet envelope-front" aria-label="Envelope, front">
  <span class="faint-mark" aria-hidden="true"></span>
  <svg class="curves" width="562" height="255" viewBox="0 0 562 255" aria-hidden="true">
    <path d="M0 198C200 240 420 250 562 205V255H0Z" fill="var(--navy)"/>
    <path d="M230 242C380 240 480 225 562 182V199C480 230 360 244 230 242Z" fill="var(--red)"/>
  </svg>
  <div class="brand"><span class="dot"></span>Corrindale Planners, LLC</div>
  <p class="address">2170 Linden Court<br>Ashgrove, NY 11620</p>
</section>

<section class="sheet envelope-back" aria-label="Envelope, back">
  <svg class="curves" width="560" height="255" viewBox="0 0 560 255" aria-hidden="true">
    <path d="M0 0H560L548 60Q543 94 510 94H50Q17 94 12 60Z" fill="var(--navy)"/>
  </svg>
  <div class="brand light"><span class="dot"></span>Corrindale Planners, LLC</div>
  <p class="web">www.corrindaleplanners.com</p>
</section>

<section class="sheet letterhead" aria-label="Letterhead">
  <span class="faint-mark" aria-hidden="true"></span>
  <svg class="curves" width="497" height="701" viewBox="0 0 497 701" aria-hidden="true">
    <path d="M0 646C170 700 380 690 497 650V701H0Z" fill="var(--navy)"/>
    <path d="M210 685C340 680 440 662 497 632V649C420 675 320 686 210 685Z" fill="var(--red)"/>
  </svg>
  <div class="brand"><span class="dot"></span>Corrindale Planners, LLC</div>
  <p class="address">2170 Linden Court<br>Ashgrove, NY 11620</p>
  <ul class="contacts">
    <li><svg width="8" height="8" viewBox="0 0 10 10"><path d="M1 3Q5 0 9 3L8 5 6 4V3H4V4L2 5Z M2 6H8V9H2Z"/></svg>555 0142 7788</li>
    <li><svg width="8" height="8" viewBox="0 0 10 10"><path d="M3 1H7V3H3Z M1 4H9V8H1Z"/></svg>555 0198 3310</li>
    <li><svg width="8" height="8" viewBox="0 0 10 10"><path d="M0 2H10V8H0Z"/></svg>marcus@corrindale.com</li>
    <li><svg width="8" height="8" viewBox="0 0 10 10"><circle cx="5" cy="5" r="5"/></svg>www.corrindaleplanners.com</li>
  </ul>
</section>

</body>
</html>
```